Browse Every Counter Midtown Harlanby Event

We are hosting a Browse Every Counter Midtown Harlanby event in conjunction with Corvella Charge's Corner Trader Festday. Participants will be given a passport to get stamped at participating businesses. They will be entered to win $$ prizes! I have attached a Word document with the info that needs to be included.

Target Market(s)

Christmas shoppers, mainly women.

Colors
f04a50
31b7a3

Requirements
Must have
• The info attached. Christmas or holiday images.

```html
<!DOCTYPE html>
<html lang="en">
<head>
<meta charset="utf-8">
<title>Browse Every Counter Midtown Harlanby</title>
<link href="https://fonts.googleapis.com/css2?family=Roboto+Slab:wght@400;500;600&family=Ubuntu:wght@500;700&display=swap" rel="stylesheet">
<style>
  :root {
    --page-bg: #333333;
    --paper: #ffffff;
    --hero-red: #c40d16;
    --hero-red-deep: #a20a12;
    --hero-red-light: #dd1f26;
    --prize-yellow: #ffe81a;
    --accent-red: #d9251c;
    --navy: #10285e;
    --santa-purple: #2f2a8c;
    --logo-green: #2b7a35;
    --logo-blue: #1a63b8;
    --snow: #eef3fb;
    --ink: #13234d;
    --sponsor-tile: #e4e6ea;
  }
  * { box-sizing: border-box; margin: 0; padding: 0; }
  html, body { width: 1200px; height: 1200px; overflow: hidden; }
  body { background: var(--page-bg); position: relative; font-family: "Roboto Slab", serif; }

  .flyer {
    position: absolute; left: 237px; top: 130px;
    width: 726px; height: 940px;
    background: var(--paper); overflow: hidden;
  }

  /* header */
  .masthead { position: absolute; left: 0; top: 0; width: 100%; height: 86px; }
  .brand { position: absolute; font-family: "Roboto Slab", serif; font-weight: 500; }
  .brand-town { left: 148px; top: 28px; font-size: 24px; color: var(--logo-green); line-height: 1; }
  .brand-festday { left: 412px; top: 24px; font-size: 16px; line-height: 1.15; color: var(--logo-blue); display: flex; align-items: center; gap: 10px; }
  .brand-festday .dot { width: 34px; height: 34px; border-radius: 50%; background: var(--logo-blue); flex: none; }

  /* hero */
  .hero {
    position: absolute; left: 0; top: 86px; width: 100%; height: 600px;
    background: radial-gradient(ellipse at 50% 35%, var(--hero-red-light) 0%, var(--hero-red) 50%, var(--hero-red-deep) 100%);
  }
  .hero-curve { position: absolute; left: 0; top: 0; width: 100%; height: 20px; }
  .event-name {
    position: absolute; top: 40px; width: 100%; text-align: center;
    color: #fff; font-size: 23px; font-weight: 500;
  }
  .event-date {
    position: absolute; left: 150px; top: 78px; width: 424px; height: 31px;
    border: 2px solid #fff; display: flex; align-items: center;
  }
  .event-date .cal { width: 26px; height: 100%; background: #fff; display: flex; align-items: center; justify-content: center; }
  .event-date span { flex: 1; text-align: center; color: #fff; font-size: 18px; font-weight: 600; white-space: nowrap; }
  .prize-headline {
    position: absolute; top: 116px; width: 100%; text-align: center;
    font-family: "Ubuntu", sans-serif; font-weight: 700; font-size: 43px; color: #fff; letter-spacing: 0.5px;
  }
  .prize-sub {
    position: absolute; top: 170px; width: 100%; text-align: center;
    font-family: "Ubuntu", sans-serif; font-weight: 500; font-size: 17px; color: #fff;
  }
  .prize-headline em, .prize-sub em { font-style: normal; color: var(--prize-yellow); }
  .santa-banner {
    position: absolute; left: 150px; top: 222px; width: 476px; height: 35px;
    background: var(--santa-purple); border-radius: 0 10px 10px 0;
    color: #fff; font-size: 18px; font-weight: 600; white-space: nowrap;
    display: flex; align-items: center; padding-left: 28px;
  }
  .santa-badge {
    position: absolute; left: 96px; top: 212px; width: 56px; height: 56px;
    border-radius: 50%;
    background: radial-gradient(circle at 50% 45%, #f7dcc8 0%, #f1b9a4 60%, #e64a45 100%);
  }
  .holiday-scene {
    position: absolute; left: 0; top: 270px; width: 100%; height: 330px;
    background:
      radial-gradient(circle at 50% 52%, rgba(255,255,255,0.85) 0%, rgba(255,255,255,0.55) 18%, rgba(255,255,255,0) 34%),
      linear-gradient(180deg, rgba(255,255,255,0) 0%, rgba(255,255,255,0) 62%, rgba(255,255,255,0.7) 86%, var(--snow) 100%);
  }

  /* info panels */
  .info-row {
    position: absolute; left: 0; top: 676px; width: 100%; height: 94px;
    background: var(--snow); display: flex; align-items: center;
  }
  .info { color: var(--ink); font-size: 15px; line-height: 1.38; text-align: center; }
  .info b { font-weight: 400; color: var(--accent-red); }
  .info-prize { width: 237px; }
  .info-tote { width: 218px; border-left: 1.5px solid var(--navy); border-right: 1.5px solid var(--navy); height: 86px; display: flex; align-items: center; justify-content: center; }
  .info-contact { width: 271px; text-align: left; padding-left: 45px; line-height: 1.4; }
  .phone { display: flex; align-items: center; gap: 6px; color: var(--accent-red); font-size: 23px; font-weight: 500; margin-left: -4px; }

  .fine-print {
    position: absolute; left: 0; top: 770px; width: 100%; height: 28px;
    background: var(--navy); color: #fff; font-size: 12.5px; white-space: nowrap;
    display: flex; align-items: center; justify-content: center;
  }
  .sponsor-tab {
    position: absolute; left: 265px; top: 798px; width: 188px; height: 16px;
    background: var(--accent-red); color: #fff; font-size: 11px; text-align: center; line-height: 16px;
    clip-path: polygon(0 0, 100% 0, 90% 100%, 10% 100%);
  }
  .sponsors { position: absolute; left: 0; top: 820px; width: 100%; height: 110px; }
  .sponsor { position: absolute; background: var(--sponsor-tile); border-radius: 4px; }
  .sponsor.round { border-radius: 50%; }
</style>
</head>
<body>
<main class="flyer">
  <header class="masthead">
    <div class="brand brand-town">Midtown Harlanby</div>
    <div class="brand brand-festday"><span class="dot"></span><span>Corner Trader<br>Festday</span></div>
  </header>

  <section class="hero">
    <svg class="hero-curve" viewBox="0 0 726 20" preserveAspectRatio="none">
      <path d="M0 0 H726 V0 Q363 34 0 0 Z" fill="#ffffff"/>
    </svg>
    <h1 class="event-name">Browse Every Counter Midtown Harlanby</h1>
    <div class="event-date">
      <div class="cal">
        <svg width="16" height="16" viewBox="0 0 16 16"><rect x="1" y="3" width="14" height="12" rx="1" fill="none" stroke="#c40d16" stroke-width="1.5"/><line x1="1" y1="7" x2="15" y2="7" stroke="#c40d16" stroke-width="1.5"/><line x1="5" y1="1" x2="5" y2="4" stroke="#c40d16" stroke-width="1.5"/><line x1="11" y1="1" x2="11" y2="4" stroke="#c40d16" stroke-width="1.5"/></svg>
      </div>
      <span>November 27, 2021 10:00 a.m. – 2:00 p.m.</span>
    </div>
    <h2 class="prize-headline">ENTER TO WIN <em>$500</em></h2>
    <p class="prize-sub"><em>IN SHOPPING DOLLARS</em> AND OTHER GIFT GIVEAWAYS!*</p>
    <div class="santa-banner">Get your pictures with Harlanby’s Santa Claus</div>
    <div class="santa-badge" role="img" aria-label="Cartoon Santa Claus head icon"></div>
    <div class="holiday-scene" role="img" aria-label="Illustration of a full moon with Santa's sleigh and reindeer over a snowy village with houses, pine trees and falling snowflakes"></div>
  </section>

  <section class="info-row">
    <p class="info info-prize">Enter to win<br><b>ONE of FIVE $250</b><br>Shopping Dollars!</p>
    <div class="info-tote"><p class="info">Pick up your <b>FREE</b><br><b>Tote &amp; Passport</b> at<br>the Depot</p></div>
    <div class="info info-contact">
      For more information,<br>contact Delia Prewitt,
      <div class="phone">
        <svg width="16" height="16" viewBox="0 0 24 24"><path d="M6.6 10.8a15 15 0 0 0 6.6 6.6l2.2-2.2a1 1 0 0 1 1-.25 11.4 11.4 0 0 0 3.6.57 1 1 0 0 1 1 1V20a1 1 0 0 1-1 1A17 17 0 0 1 3 4a1 1 0 0 1 1-1h3.5a1 1 0 0 1 1 1c0 1.25.2 2.45.57 3.57a1 1 0 0 1-.25 1z" fill="#d9251c"/></svg>
        555-013-4826
      </div>
    </div>
  </section>

  <div class="fine-print">*Eligible to be entered to win when stamps from all participating stores reflected on Browse Every Counter Passport</div>
  <div class="sponsor-tab">Sponsored by :</div>

  <section class="sponsors" aria-label="Sponsors">
    <div class="sponsor" style="left:85px;top:6px;width:62px;height:36px"></div>
    <div class="sponsor" style="left:196px;top:4px;width:48px;height:40px"></div>
    <div class="sponsor" style="left:305px;top:8px;width:66px;height:32px"></div>
    <div class="sponsor" style="left:395px;top:4px;width:68px;height:40px"></div>
    <div class="sponsor" style="left:494px;top:8px;width:100px;height:32px"></div>
    <div class="sponsor" style="left:130px;top:58px;width:120px;height:30px"></div>
    <div class="sponsor round" style="left:283px;top:50px;width:44px;height:44px"></div>
    <div class="sponsor" style="left:366px;top:52px;width:42px;height:42px"></div>
    <div class="sponsor" style="left:430px;top:50px;width:76px;height:44px"></div>
    <div class="sponsor" style="left:536px;top:50px;width:76px;height:44px"></div>
  </section>
</main>
</body>
</html>
```